Premium Van Wrap Design for Drone Cleaning Business (Dual Branding Concept)

We are looking for a highly creative and experienced graphic designer to develop a visually striking, premium van wrap design for a drone-based cleaning business.
The vehicle will act primarily as a mobile demonstration unit, showcasing cutting-edge drone cleaning solutions across multiple industries including wind turbines, warehouses, building façades, and solar farms.
The design must communicate innovation, efficiency, and industrial capability, while remaining clean, modern, and highly professional.
CORE CHALLENGE (Key Requirement)
This project requires a flexible dual-branding solution.
The van will operate under two brands:
- Primary (Demo Mode): SkyRinseWorks.net (no logo yet)
- Secondary (Commercial Work): The Copper Kestrel
The design must allow branding to be switched using magnetic overlay panels therefore consideration for van panels (Valtoria Carrex T7R2).
This means:
- The base wrap should be visually complete without relying on fixed branding in key areas
- Specific zones must be designed where magnetic panels can be applied seamlessly
- The switch between brands must look intentional and premium, not like an afterthought
Designers must account for this modular branding approach from the outset.
DESIGN OBJECTIVES
The wrap should:
- Look high-end and technologically advanced
- Clearly communicate drone-based cleaning solutions
- Showcase multiple use cases visually:
- Wind turbines
- Industrial warehouses
- Building façades
- Solar panels
- Feel dynamic and eye-catching even at distance
- Avoid clutter while still telling a strong visual story
- Work across all van surfaces (sides, rear, bonnet if applicable)
STYLE DIRECTION
We are aiming for:
- Clean, modern, and bold
- Industrial + tech aesthetic
- Subtle gradients, depth, and motion where appropriate
- Strong visual hierarchy
- Minimal but impactful text
Avoid:
- Overly busy layouts
- Clip-art style graphics
- Low-end “signage” look
Think premium fleet branding rather than standard van graphics.
FUNCTIONAL REQUIREMENTS
- Design must include clearly defined zones for magnetic overlays
- Branding areas should be easy to swap without disrupting the overall design
- Consider how logos, taglines, and contact details will adapt between brands
- Ensure readability at distance and in motion
- Must be print-ready for professional vehicle wrapping
DELIVERABLES
- Full van wrap design (all sides, rear, optional bonnet)
- Layered source files (Adobe Illustrator preferred)
- Print-ready files with correct dimensions and bleed
- Visual mockups (realistic render of van we can supply a 3D Model of van)
- Clear indication of magnetic overlay zones
INFORMATION TO BE PROVIDED
We will supply:
- Logos for The Copper Kestrel - you have free reign over SkyRinseWorks.net
Vehicle dimensions/template (also 3D model of van available on request for renders)
IDEAL DESIGNER
We are looking for someone who:
- Has strong experience in vehicle wrap design
- Demonstrates high-end branding work
- Understands spatial design and large-format layouts
- Can think creatively about modular branding systems

```html
<!DOCTYPE html>
<html lang="en">
<head>
<meta charset="utf-8">
<title>The Copper Kestrel – Van Side Wrap</title>
<link rel="stylesheet" href="https://fonts.googleapis.com/css2?family=Bebas+Neue&family=Poppins:wght@500;600;700&display=swap">
<style>
  :root {
    --page: #e9ecef;
    --wrap-white: #ffffff;
    --ink: #1f2a33;
    --brand-blue: #2f8fd6;
    --glass-deep: #1d4fa0;
    --glass-light: #6f9fd8;
    --frame-grey: #8a8f94;
    --drone-dark: #2b2e31;
    --drone-light: #9aa0a5;
    --panel-line: #d5d9dd;
  }
  * { margin: 0; padding: 0; box-sizing: border-box; }
  html, body { width: 1200px; height: 822px; overflow: hidden; background: var(--page); }
  .wrap-side {
    position: absolute; left: 40px; top: 70px; width: 1120px; height: 682px;
    background: var(--wrap-white); border-radius: 28px; overflow: hidden;
    border: 1px solid var(--panel-line);
  }
  .wrap-side svg.art { position: absolute; inset: 0; }
  .headline {
    position: absolute; left: 341px; top: 166px;
    font-family: "Bebas Neue", "Arial Narrow", sans-serif; font-weight: 400;
    color: var(--ink); font-size: 47px; line-height: 54px; letter-spacing: 0.3px;
  }
  .phone {
    position: absolute; left: 505px; top: 356px;
    font-family: "Poppins", Arial, sans-serif; font-weight: 700;
    color: var(--brand-blue); font-size: 45px; line-height: 1; letter-spacing: 0.5px;
    white-space: nowrap;
  }
  .brand-zone {
    position: absolute; left: 66px; top: 462px; display: flex; align-items: center; gap: 10px;
    font-family: "Poppins", Arial, sans-serif; font-weight: 600;
    color: var(--ink); font-size: 15px; letter-spacing: 0.5px; text-transform: uppercase;
    white-space: nowrap;
  }
  .brand-zone .dot { width: 13px; height: 13px; border-radius: 50%; background: var(--ink); }
  .services {
    position: absolute; left: 378px; top: 432px; display: flex; list-style: none;
  }
  .service { display: flex; align-items: center; gap: 10px; width: 147px; }
  .service svg { width: 64px; height: 74px; flex: none; }
  .service-label {
    font-family: "Poppins", Arial, sans-serif; font-weight: 600;
    font-size: 11px; line-height: 14px; color: var(--ink); text-transform: uppercase;
    white-space: nowrap;
  }
</style>
</head>
<body>
<main class="wrap-side">
  <svg class="art" width="1120" height="682" viewBox="0 0 1120 682">
    <defs>
      <linearGradient id="glassGrad" x1="0" y1="0" x2="1" y2="1">
        <stop offset="0" stop-color="var(--frame-grey)"/>
        <stop offset="0.45" stop-color="var(--glass-light)"/>
        <stop offset="1" stop-color="var(--glass-deep)"/>
      </linearGradient>
      <linearGradient id="droneGrad" x1="0" y1="0" x2="0" y2="1">
        <stop offset="0" stop-color="var(--drone-light)" stop-opacity="0.55"/>
        <stop offset="1" stop-color="var(--drone-dark)" stop-opacity="0.35"/>
      </linearGradient>
    </defs>
    <polygon class="facade-photo" role="img" aria-label="Photo of a glass building facade being sprayed with water"
             points="1035,23 1120,23 1120,412 857,412" fill="url(#glassGrad)"/>
    <rect class="drone-photo" role="img" aria-label="Photo of a cleaning drone with a spray lance aimed at the facade"
          x="535" y="14" width="380" height="280" rx="18" fill="url(#droneGrad)"/>
    <rect class="window-rail" x="634" y="318" width="303" height="8" rx="4" fill="var(--ink)"/>
  </svg>

  <h1 class="headline">Drone<br>Cleaning<br>Technology</h1>
  <p class="phone">01632 960418</p>

  <div class="brand-zone"><span class="dot"></span><span>The Copper Kestrel</span></div>

  <ul class="services">
    <li class="service">
      <svg viewBox="0 0 58 64"><polygon points="29,2 55,17 55,47 29,62 3,47 3,17" fill="none" stroke="var(--brand-blue)" stroke-width="2.5"/>
        <g stroke="var(--brand-blue)" stroke-width="2.5" stroke-linecap="round"><line x1="29" y1="30" x2="29" y2="50"/><line x1="29" y1="30" x2="29" y2="14"/><line x1="29" y1="30" x2="16" y2="37"/><line x1="29" y1="30" x2="42" y2="37"/></g></svg>
      <span class="service-label">Wind<br>Turbine<br>Cleaning</span>
    </li>
    <li class="service">
      <svg viewBox="0 0 58 64"><polygon points="29,2 55,17 55,47 29,62 3,47 3,17" fill="none" stroke="var(--brand-blue)" stroke-width="2.5"/>
        <g fill="none" stroke="var(--brand-blue)" stroke-width="2.2"><polyline points="12,28 29,19 46,28"/><rect x="15" y="28" width="28" height="16"/><rect x="22" y="36" width="14" height="6"/></g></svg>
      <span class="service-label">Warehouse<br>Cleaning</span>
    </li>
    <li class="service">
      <svg viewBox="0 0 58 64"><polygon points="29,2 55,17 55,47 29,62 3,47 3,17" fill="none" stroke="var(--brand-blue)" stroke-width="2.5"/>
        <g fill="none" stroke="var(--brand-blue)" stroke-width="2.2"><rect x="19" y="18" width="20" height="27"/><line x1="19" y1="25" x2="39" y2="25"/><line x1="19" y1="32" x2="39" y2="32"/><line x1="19" y1="39" x2="39" y2="39"/><line x1="14" y1="46" x2="44" y2="46"/></g></svg>
      <span class="service-label">Facade<br>Cleaning</span>
    </li>
    <li class="service">
      <svg viewBox="0 0 58 64"><polygon points="29,2 55,17 55,47 29,62 3,47 3,17" fill="none" stroke="var(--brand-blue)" stroke-width="2.5"/>
        <g fill="none" stroke="var(--brand-blue)" stroke-width="2"><polygon points="16,28 42,28 45,40 13,40"/><line x1="29" y1="28" x2="29" y2="40"/><line x1="15" y1="34" x2="43" y2="34"/><line x1="29" y1="40" x2="29" y2="47"/><line x1="23" y1="47" x2="35" y2="47"/><circle cx="29" cy="20" r="3"/></g></svg>
      <span class="service-label">Solar<br>Panel<br>Cleaning</span>
    </li>
  </ul>
</main>
</body>
</html>
```